Harbourline Optical -Window Poster (Optometrist)

We are an optometry practice and we need a poster for a new store promotion for our window highlighting we now also sell 2 pairs of glasses as a package deal. The size will be 1300mm width x 1900mm height

The artwork will be displayed as a fabric banner in our shop window. We have 7 other banners with different services our business provides. The words needs to standout for passers by and the cars stopped at the traffic lights out front of our business. We already have signs with our logos phone number etc. so we won't need them included in the poster.

It would need to include the following information.

Two pair packages now available*

*Conditions apply

The artwork will be displayed as a fabric banner in our shop window. We have 7 other banners with different services our business provides. The words needs to standout for passers by and the cars stopped at the traffic lights out front of our business. We already have signs with our logos phone number etc. so we won't need them included in the poster. Thank you for your work it's amazing Added Saturday, February 18, 2017

The artwork will be displayed as a fabric banner in our shop window. We have 7 other banners with different services our business provides. The words needs to standout for passers by and the cars stopped at the traffic lights out front of our business. We already have signs with our logos phone number etc. so we won't need them included in the poster. Added Saturday, February 18, 2017

Target Market(s)

Cars driving past and stopped at traffic lights outside our store.

Industry/Entity Type

Optician

Requirements
Must have
• Poster must say:
• Two pair packages now available*
• *Conditions apply

```html
<!DOCTYPE html>
<html lang="en">
<head>
<meta charset="utf-8">
<title>Harbourline Optical – Two Pair Packages Window Poster</title>
<link rel="stylesheet" href="https://fonts.googleapis.com/css2?family=Alfa+Slab+One&family=Anton&family=Oswald:wght@500&display=swap">
<style>
  :root {
    --sky-deep: #2b2f8f;
    --sky-mid: #3f63c2;
    --sky-light: #6f8fd0;
    --horizon: #7d8590;
    --wood-light: #a8966a;
    --wood-mid: #8d7d55;
    --wood-dark: #5e5439;
    --headline-yellow: #ffec00;
    --panel-white: #f2f3f5;
    --frame-white: #ffffff;
    --ink-black: #050505;
    --promo-red: #e8202a;
  }
  html, body {
    margin: 0;
    padding: 0;
    width: 962px;
    height: 1200px;
    overflow: hidden;
    background: #ffffff;
  }
  .poster {
    display: block;
    width: 962px;
    height: 1200px;
  }
  .availability-line {
    font-family: "Alfa Slab One", "Rockwell", serif;
    fill: var(--headline-yellow);
  }
  .offer-line {
    font-family: "Anton", "Impact", sans-serif;
  }
  .offer-line--black { fill: var(--ink-black); }
  .offer-line--red { fill: var(--promo-red); }
  .offer-line--shadow { fill: var(--ink-black); }
  .conditions-note {
    font-family: "Oswald", "Arial Narrow", sans-serif;
    font-weight: 500;
    fill: var(--ink-black);
    letter-spacing: 2px;
  }
</style>
</head>
<body>
<svg class="poster" viewBox="0 0 962 1200" xmlns="http://www.w3.org/2000/svg" aria-labelledby="posterTitle">
  <title id="posterTitle">Two pair packages now available – conditions apply</title>
  <defs>
    <linearGradient id="backdropGradient" x1="0" y1="0" x2="0" y2="1">
      <stop offset="0" stop-color="var(--sky-deep)"/>
      <stop offset="0.12" stop-color="var(--sky-light)"/>
      <stop offset="0.3" stop-color="var(--sky-mid)"/>
      <stop offset="0.42" stop-color="var(--sky-mid)"/>
      <stop offset="0.5" stop-color="var(--horizon)"/>
      <stop offset="0.62" stop-color="var(--wood-mid)"/>
      <stop offset="0.8" stop-color="var(--wood-light)"/>
      <stop offset="1" stop-color="var(--wood-dark)"/>
    </linearGradient>
  </defs>

  <!-- backdrop -->
  <rect class="backdrop" x="0" y="0" width="962" height="1200" fill="url(#backdropGradient)"
        role="img" aria-label="Photo of a bright blue sky above a weathered wooden surface"/>

  <!-- availability banner -->
  <g class="availability-banner" fill="none" stroke="var(--frame-white)" stroke-width="3">
    <polyline points="274,169 63,169 63,65 854,65 854,169 643,169"/>
  </g>
  <text class="availability-line" x="105" y="146" font-size="72"
        textLength="731" lengthAdjust="spacingAndGlyphs">NOW AVAILABLE*</text>

  <!-- offer card -->
  <polygon class="offer-card-frame" points="54,257 849,197 914,795 118,852"
           fill="none" stroke="var(--frame-white)" stroke-width="3"/>
  <rect class="offer-card" x="83" y="225" width="802" height="601" fill="var(--panel-white)"/>

  <text class="offer-line offer-line--black" x="108" y="480" font-size="188"
        textLength="755" lengthAdjust="spacingAndGlyphs">TWO PAIR</text>

  <text class="offer-line offer-line--shadow" x="107" y="673" font-size="174"
        textLength="755" lengthAdjust="spacingAndGlyphs" aria-hidden="true">PACKAGES</text>
  <text class="offer-line offer-line--red" x="114" y="664" font-size="174"
        textLength="755" lengthAdjust="spacingAndGlyphs">PACKAGES</text>

  <!-- conditions note -->
  <g class="conditions-frame" fill="none" stroke="var(--ink-black)" stroke-width="2.5">
    <polyline points="374,971 254,971 254,1075 710,1075 710,971 592,971"/>
  </g>
  <text class="conditions-note" x="254" y="1046" font-size="50"
        textLength="447" lengthAdjust="spacingAndGlyphs">*CONDITIONS APPLY</text>
</svg>
</body>
</html>
```